New Email Marketing Design Project

I’d like you to make an email template. I’ll be welcoming and on boarding customers via email. And I’d like the branding to stand out. Keep it professional and simple. But be creative.

Design should look amazing on desktop and mobile phones.

Negative white space is ok.

Use stock images

I’ll like to have a spot for a picture of myself so make sure to include a circle where I can show my face so that email viewers will know who is speaking to them.

Target Market(s)

Practice managers, doctors, medical providers

Font styles to use
Sans Serif

Requirements
Must have
• Our Logo, CTA buttons, Same colors as website.
https://www.tarvoclaimpartnersgroup.com

```html
<!DOCTYPE html>
<html lang="en">
<head>
<meta charset="utf-8">
<title>Tarvo Claim Partners Group – Welcome Email</title>
<link rel="stylesheet" href="https://fonts.googleapis.com/css2?family=Roboto:wght@400;500;700&family=Source+Sans+3:wght@400;600&display=swap">
<style>
  :root{
    --stage:#565656;
    --brand:#2f78a0;
    --brand-dark:#2a6a8e;
    --hero:#3f6c6a;
    --ink:#222;
    --body:#4a4a4a;
    --nav:#ececec;
    --panel:#f5f5f5;
    --line:#d6d6d6;
    --footer:#353535;
    --white:#fff;
    --dark-btn:#2d2d2d;
  }
  *{box-sizing:border-box;margin:0;padding:0}
  html,body{width:832px;height:1200px;overflow:hidden}
  body{background:radial-gradient(circle at 50% 50%,#6a6a6a 0%,var(--stage) 70%);font-family:"Roboto",Arial,sans-serif;position:relative}
  .email{position:absolute;left:236px;top:14px;width:600px;transform:scale(.6);transform-origin:0 0;background:var(--white);box-shadow:0 0 40px rgba(0,0,0,.45)}
  .header{height:105px;position:relative;background:var(--white)}
  .brand{position:absolute;left:30px;top:22px;display:flex;align-items:center;gap:10px}
  .brand-dot{width:56px;height:56px;border-radius:50%;background:var(--brand)}
  .brand-name{font-weight:700;font-size:17px;color:var(--brand);line-height:1.15;width:140px}
  .help{position:absolute;right:0;top:0;width:295px;height:105px;background:var(--brand);clip-path:polygon(50px 0,100% 0,100% 100%,0 100%)}
  .help-icon{position:absolute;left:58px;top:30px}
  .help-label{position:absolute;left:93px;top:24px;color:var(--white);font-size:16px}
  .help-phone{position:absolute;left:93px;top:42px;color:var(--white);font-size:29px;font-weight:700;letter-spacing:.5px}
  .nav{height:51px;background:var(--nav);display:flex;justify-content:center;align-items:center;gap:30px;font-size:15px;color:var(--ink)}
  .nav .active{color:var(--brand)}
  .hero{height:280px;position:relative;background:linear-gradient(120deg,#4a7876 0%,var(--hero) 60%,#37605e 100%)}
  .hero-title{position:absolute;left:17px;top:77px;color:var(--white);font-size:29px;font-weight:700;line-height:34px}
  .hero-text{position:absolute;left:17px;top:150px;width:310px;color:var(--white);font-family:"Source Sans 3",sans-serif;font-size:15.5px;line-height:20px}
  .portrait{position:absolute;left:347px;top:34px;width:218px;height:218px;border-radius:50%;border:10px solid rgba(210,220,215,.55);background:radial-gradient(circle at 50% 40%,#e8eef2 0%,#bfd0da 60%,#8fa9b8 100%)}
  .intro{height:328px;text-align:center;padding-top:54px}
  .intro p{width:500px;margin:0 auto;font-family:"Source Sans 3",sans-serif;font-size:15px;line-height:22px;color:var(--body)}
  .btn{display:inline-flex;align-items:center;gap:8px;height:47px;padding:0 15px;font-weight:700;font-size:16px;color:var(--white);background:var(--brand);border:1px solid var(--brand-dark);border-radius:2px}
  .intro .btn{margin-top:28px;width:179px;justify-content:center}
  .services{height:747px;background:var(--panel);padding-top:52px;text-align:center}
  .services h2{font-size:21px;font-weight:500;color:var(--ink);margin-bottom:45px}
  .service-grid{width:568px;margin:0 auto;display:grid;grid-template-columns:1fr 1fr;border-top:1px solid var(--line)}
  .service{height:150px;border-bottom:1px solid var(--line);padding-top:25px}
  .service:nth-child(odd){border-right:1px solid var(--line)}
  .service-icon{width:68px;height:68px;border-radius:50%;margin:0 auto;background:var(--white);border:1px solid #ddd;display:flex;align-items:center;justify-content:center}
  .service-icon span{width:36px;height:36px;border-radius:6px;background:#d9e8f1}
  .service-name{margin-top:22px;font-size:14.5px;font-weight:700;color:var(--ink)}
  .services .btn{margin-top:50px;width:179px;justify-content:center;gap:22px}
  .cta{height:217px;background:linear-gradient(135deg,#3580aa 0%,var(--brand) 50%,#2a6f96 100%);text-align:center;padding-top:64px}
  .cta h2{color:var(--white);font-size:36px;font-weight:700}
  .cta .btn{margin-top:14px;background:var(--dark-btn);border-color:var(--dark-btn);width:178px;justify-content:center}
  .info{height:132px;position:relative;text-align:center}
  .info-mark{position:absolute;top:42px;width:60px;height:54px;border-radius:50%;background:#cfe1ec}
  .info-mark.left{left:20px}.info-mark.right{right:30px}
  .info-label{padding-top:42px;color:var(--brand);font-size:17.5px;font-weight:500}
  .info-url{font-size:21.5px;font-weight:500;color:var(--ink);margin-top:4px}
  .footer{height:95px;background:var(--footer);text-align:center;padding-top:26px}
  .social{display:flex;justify-content:center;gap:10px}
  .social span{width:22px;height:22px;border-radius:50%;background:var(--white)}
  .copyright{margin-top:12px;color:var(--white);font-size:14px}
</style>
</head>
<body>
<main class="email">
  <header class="header">
    <div class="brand"><span class="brand-dot"></span><span class="brand-name">Tarvo Claim Partners Group</span></div>
    <div class="help">
      <svg class="help-icon" width="22" height="42" viewBox="0 0 22 42"><rect x="2" y="2" width="18" height="38" rx="3" fill="none" stroke="#fff" stroke-width="3"/><line x1="7" y1="7" x2="15" y2="7" stroke="#fff" stroke-width="2"/><circle cx="11" cy="34" r="2" fill="#fff"/></svg>
      <div class="help-label">Need Help? Call Us Now</div>
      <div class="help-phone">15550142277</div>
    </div>
  </header>
  <nav class="nav"><span class="active">HOME</span><span>SERVICE</span><span>ABOUT US</span><span>CAREERS</span><span>BLOG</span><span>CONTACT US</span></nav>
  <section class="hero" role="img" aria-label="Desk with calculator and paperwork behind the introduction">
    <h1 class="hero-title">TARVO CLAIM<br>PARTNERS GROUP</h1>
    <p class="hero-text">Tarvo Claim Partners Group will allow you to save on overhead expenses such as salaries, payroll taxes, benefits, and printing/office supplies.</p>
    <div class="portrait" role="img" aria-label="Circular portrait of the sender"></div>
  </section>
  <section class="intro">
    <p>At Tarvo Claim Partners Group we are focused on providing medical billing services with the highest levels of customer satisfaction &amp; we will do everything we can to meet your expectations. With a variety of offerings to choose from, we're sure you'll be happy working with us. Tarvo Claim Partners Group is a company that you can place your trust in. We offer comprehensive and secure billing support</p>
    <a class="btn">SUBSCRIBE NOW <svg width="16" height="16" viewBox="0 0 16 16"><circle cx="8" cy="8" r="8" fill="#fff"/><path d="M4 8h7M8 5l3 3-3 3" stroke="#2f78a0" stroke-width="2" fill="none"/></svg></a>
  </section>
  <section class="services">
    <h2>OUR SERVICES</h2>
    <div class="service-grid">
      <div class="service"><div class="service-icon" role="img" aria-label="Eligibility check icon"><span></span></div><div class="service-name">INSURANCE ELIGIBILITY CHECK</div></div>
      <div class="service"><div class="service-icon" role="img" aria-label="Clearinghouse icon"><span></span></div><div class="service-name">CLEARINGHOUSE MAINTENANCE</div></div>
      <div class="service"><div class="service-icon" role="img" aria-label="Medical billing icon"><span></span></div><div class="service-name">MEDICAL BILLING</div></div>
      <div class="service"><div class="service-icon" role="img" aria-label="Patient collections icon"><span></span></div><div class="service-name">PATIENT COLLECTIONS</div></div>
      <div class="service"><div class="service-icon" role="img" aria-label="Credentialing icon"><span></span></div><div class="service-name">INSURANCE CREDENTIALING</div></div>
      <div class="service"><div class="service-icon" role="img" aria-label="Claim denial icon"><span></span></div><div class="service-name">CLAIM DENIAL</div></div>
    </div>
    <a class="btn">VIEW MORE <svg width="16" height="16" viewBox="0 0 16 16"><circle cx="8" cy="8" r="8" fill="#fff"/><path d="M4 8h7M8 5l3 3-3 3" stroke="#2f78a0" stroke-width="2" fill="none"/></svg></a>
  </section>
  <section class="cta" role="img" aria-label="Blue tinted desk scene with calculator">
    <h2>READY TO GET STARTED?</h2>
    <a class="btn">SUBSCRIBE NOW <svg width="16" height="16" viewBox="0 0 16 16"><circle cx="8" cy="8" r="8" fill="#fff"/><path d="M4 8h7M8 5l3 3-3 3" stroke="#2d2d2d" stroke-width="2" fill="none"/></svg></a>
  </section>
  <section class="info">
    <span class="info-mark left" role="img" aria-label="Medical emblem decoration"></span>
    <span class="info-mark right" role="img" aria-label="Medical emblem decoration"></span>
    <div class="info-label">FOR MORE INFORMATION VISIT</div>
    <div class="info-url">WWW.TARVOCLAIMPARTNERSGROUP.COM</div>
  </section>
  <footer class="footer">
    <div class="social"><span></span><span></span><span></span><span></span></div>
    <div class="copyright">© 2020 tarvoclaimpartnersgroup</div>
  </footer>
</main>
</body>
</html>
```